Delivery Docket urgent plus require many other designs for more stationary after this.

We need a new delivery docket design urgently as the one we have needs updating and we have changed our company name. Please do not copy the one I have uploaded as we do not feel this looks professional enough. I uploaded it as a few designers requested to see what we are currently using thank you.
It is quite complex in that we need a range of information to be on the one docket.
We are a Transport Company based in Australia that has a wide variety of items that we deliver such as water, sand and gravels and heavy equipment transport.
We would prefer to keep this design to A5 size as we will get them made into books. We are looking for a modern professional look. Although it is only a delivery docket this is given to all our customers so needs to look impressive.

We need our new logo on the docket (PRW). There will also need to be areas for our address and contact numbers, email etc these will be supplied to the winning designer to make the final adjustments so for now just put something generic in these spaces.
Needs to have an area for customer details, purchase order number, date and docket number (docket number to be in red)
Needs a section where we can list the type of product / and or service that has been provided and the amount / qty usually 3 lines will be enough for this. Need area under this where the customer can sign name and print name to say that the goods / and or services have been received.

Also required somewhere on the docket are the words, Tax Invoice will be issued based on the information provided on this docket. Conditions on back of page

We then need a separate section on the same page which we will use internally that the staff member can tear off and hand into the office. On this section it needs to have area where the driver can list km at start of job and at end with space to calculate km travelled, details of fuel purchased eg amount and litres, vehicle that is being used. also need to log down wheel bearing temps.
prime mover needs spaces as follows
Steer axel FL____________ Steer axel FR _________ 1st drive axel L_______
1st drive axel R_________ 2nd drive axel L_______ 2nd drive axel R________

For the trailers need something similar x 2 as have 2 trailers
1st axel DS_________ 1st axel PS_________ 2nd axel DS__________
2nd axel PS_________ 3rd axel DS_________ 3rd axel PS__________

I have included a few examples of designs we have used in past and ones that we like so you can get an idea of the colours we prefer, I have included some of the designs we are currently receiving for our logo that I like so you can get idea again of colours we prefer. There is much more we need designed also such as time sheets, more delivery dockets and letter heads so there is a lot of more work available to the winning designer.

Thank you

Target Market(s)

Customers

Font styles to use
Serif
Sans Serif

Colors

Designer to choose colors to be used in the design.

Requirements
Should not have
• Please don't copy old docket as we do not like it and nned new info on new design thank you

```html
<!DOCTYPE html>
<html lang="en">
<head>
<meta charset="utf-8">
<title>PRW Delivery Docket</title>
<link href="https://fonts.googleapis.com/css2?family=Roboto+Condensed:wght@400;700&display=swap" rel="stylesheet">
<style>
  :root{
    --brand:#1474c4;
    --ink:#161616;
    --rule:#222;
    --paper:#ffffff;
    --backdrop:#ebebeb;
    --docket-red:#e0787a;
    --faint:#eef2f8;
  }
  *{box-sizing:border-box;margin:0;padding:0}
  html,body{width:1200px;height:900px;overflow:hidden}
  body{background:var(--backdrop);font-family:"Roboto Condensed",Arial,sans-serif;color:var(--ink);position:relative}
  .page{position:absolute;top:162px;width:540px;height:576px;background:var(--paper)}
  .page--docket{left:55px}
  .page--log{left:605px}
  .abs{position:absolute}

  .brand{display:flex;align-items:center;gap:10px}
  .brand__square{width:22px;height:22px;background:var(--brand)}
  .brand__name{font-weight:700;font-size:64px;line-height:1;color:var(--brand);letter-spacing:1px}

  .customer-box{left:173px;top:23px;width:353px;height:83px;border:1.2px solid var(--rule);padding:10px 10px}
  .customer-box h2{font-size:15px;font-weight:400;margin-bottom:8px}
  .field{display:inline-flex;align-items:flex-end;font-size:11px;white-space:nowrap}
  .field__line{display:inline-block;border-bottom:1px solid var(--rule);height:11px;margin-left:2px;margin-right:6px;font-size:9px;color:var(--docket-red);text-align:center;line-height:11px}
  .customer-box .row{display:flex;margin-bottom:6px}

  .contact-row{left:30px;top:121px;display:flex}
  .address-row{left:30px;top:141px}

  .items{left:16px;top:164px;width:510px;height:284px;border-collapse:collapse;table-layout:fixed}
  .items th,.items td{border:1.2px solid var(--rule)}
  .items th{height:33px;color:var(--brand);font-size:12px;font-weight:700}
  .items th.amount{font-size:11px;font-weight:400}
  .items td{height:35.8px}
  .items .qty{width:61px}
  .items .amount{width:51px}
  .items-mark{left:120px;top:178px;width:300px;text-align:center;font-size:200px;font-weight:700;color:var(--faint);line-height:1;pointer-events:none}
  .items{background:transparent}

  .note{left:0;width:540px;text-align:center;font-size:11.5px}
  .sign-row{left:27px;top:534px;display:flex;font-size:11px;color:#333}
  .sign-row .field{font-size:11px}

  .log-brand{left:194px;top:60px}
  .log-heading{left:16px;font-size:14px;font-weight:700;color:var(--brand)}
  .temp-grid{left:16px;width:512px;display:grid;grid-template-columns:1fr 1fr 1fr;row-gap:8px;column-gap:4px}
  .temp-grid .field{font-size:11px}
  .temp-grid .field__line{flex:1;margin-right:0}
</style>
</head>
<body>

<section class="page page--docket">
  <div class="brand abs" style="left:16px;top:32px">
    <span class="brand__square"></span>
    <span class="brand__name">PRW</span>
  </div>

  <div class="customer-box abs">
    <h2>Customer Details:</h2>
    <div class="row">
      <span class="field">Purchase Order Number:<span class="field__line" style="width:58px">2050</span></span>
      <span class="field">Docket Number:<span class="field__line" style="width:55px"></span></span>
    </div>
    <div class="row">
      <span class="field">Date:<span class="field__line" style="width:60px"></span></span>
    </div>
  </div>

  <div class="contact-row abs">
    <span class="field">Contact Number:<span class="field__line" style="width:122px"></span></span>
    <span class="field">Email:<span class="field__line" style="width:96px"></span></span>
    <span class="field">ABN:<span class="field__line" style="width:90px"></span></span>
  </div>
  <div class="address-row abs">
    <span class="field">Address:<span class="field__line" style="width:410px"></span></span>
  </div>

  <div class="items-mark abs" aria-hidden="true">PRW</div>
  <table class="items abs">
    <thead>
      <tr><th class="qty">Qty</th><th>Description</th><th class="amount">Amount</th></tr>
    </thead>
    <tbody>
      <tr><td></td><td></td><td></td></tr>
      <tr><td></td><td></td><td></td></tr>
      <tr><td></td><td></td><td></td></tr>
      <tr><td></td><td></td><td></td></tr>
      <tr><td></td><td></td><td></td></tr>
      <tr><td></td><td></td><td></td></tr>
      <tr><td></td><td></td><td></td></tr>
    </tbody>
  </table>

  <p class="note abs" style="top:462px">Tax Invoice will be issued based on the information provided on this docket.</p>
  <p class="note abs" style="top:481px">Conditions on back of page</p>

  <div class="sign-row abs">
    <span class="field">Print Name:<span class="field__line" style="width:203px"></span></span>
    <span class="field">Sign Name:<span class="field__line" style="width:188px"></span></span>
  </div>
</section>

<section class="page page--log">
  <div class="brand log-brand abs">
    <span class="brand__square"></span>
    <span class="brand__name">PRW</span>
  </div>

  <h3 class="log-heading abs" style="top:212px">Prime Mover Needs Spaces As Follows:</h3>
  <div class="temp-grid abs" style="top:248px">
    <span class="field">Steer axel FL<span class="field__line"></span></span>
    <span class="field">Steer axel FR<span class="field__line"></span></span>
    <span class="field">1st drive axel L<span class="field__line"></span></span>
    <span class="field">1st drive axel R<span class="field__line"></span></span>
    <span class="field">2nd drive axel L<span class="field__line"></span></span>
    <span class="field">2nd drive axel R<span class="field__line"></span></span>
  </div>

  <h3 class="log-heading abs" style="top:338px">For The Trailers Need Something Similar X 2 As Have 2 Trailers:</h3>
  <div class="temp-grid abs" style="top:374px;row-gap:18px">
    <span class="field">1st axel DS<span class="field__line"></span></span>
    <span class="field">1st axel PS<span class="field__line"></span></span>
    <span class="field">2nd axel DS<span class="field__line"></span></span>
    <span class="field">2nd axel PS<span class="field__line"></span></span>
    <span class="field">3rd axel DS<span class="field__line"></span></span>
    <span class="field">3rd axel PS<span class="field__line"></span></span>
  </div>
</section>

</body>
</html>
```